Electrical company business card design.

Hi, were an electrical company in Auckland New Zealand called Quarneth Ltd. We focus mainly on high end residential and commercial so the card would be targeted towards that.
The card will be for myself, i am the director of the company.
Name: Derek Olstow
Position: Director/electrician
Phone: 021 387 9415
Email: derek@quarneth.co.nz
Location: Auckland
As for colors the the blue color in the logo is preferred, i also don't mind a black background option.
Target Market(s)
High end residential and commercial
Industry/Entity Type
Electrician
Contact Information for Business Card
Name: Derek Olstow Position: Director/Electrician Phone: 021 387 9415, Email: derek@quarneth.co.nz, Location: Auckland

```html
<!DOCTYPE html>
<html lang="en">
<head>
<meta charset="utf-8">
<title>Quarneth Ltd — Business Card</title>
<link href="https://fonts.googleapis.com/css2?family=Montserrat:wght@400;500;700;800&display=swap" rel="stylesheet">
<style>
  :root {
    --page-bg: #d9dadc;
    --card-white: #f7f7f7;
    --card-black: #1c1a1b;
    --brand-blue: #2a7fd0;
    --ink-grey: #4d5156;
    --ink-white: #f2f2f2;
    --rule: #3a3c44;
  }
  * { margin: 0; padding: 0; box-sizing: border-box; }
  html, body {
    width: 1200px; height: 900px; overflow: hidden;
    background: var(--page-bg);
    font-family: "Montserrat", sans-serif;
  }
  .stage {
    width: 1200px; height: 900px;
    display: flex; flex-direction: column;
    align-items: center; justify-content: center; gap: 50px;
  }
  .card {
    width: 630px; height: 360px;
    border-radius: 34px;
    display: flex; flex-direction: column;
    align-items: center; justify-content: center;
    box-shadow: 0 10px 26px rgba(0,0,0,.22);
  }
  .card--front {
    background: linear-gradient(135deg, #ffffff 0%, var(--card-white) 60%, #e9e9e9 100%);
  }
  .brand-lockup { display: flex; align-items: center; gap: 18px; }
  .brand-dot {
    width: 26px; height: 26px; border-radius: 50%;
    background: var(--brand-blue);
  }
  .brand-name {
    font-weight: 800; font-size: 58px; letter-spacing: 2px;
    color: var(--ink-grey); line-height: 1;
  }
  .tagline {
    margin-top: 10px; margin-left: 44px;
    font-weight: 700; font-size: 15px; letter-spacing: 2.4px;
    color: var(--ink-grey);
  }
  .card--back { background: var(--card-black); padding-top: 10px; }
  .back-brand {
    font-weight: 800; font-size: 40px; letter-spacing: 2px;
    color: var(--ink-white); margin-bottom: 34px;
  }
  .identity { font-size: 19px; color: var(--ink-white); display: flex; gap: 10px; align-items: baseline; }
  .identity__name { color: var(--brand-blue); font-weight: 700; letter-spacing: .5px; }
  .divider {
    width: 340px; height: 1px; margin: 16px 0;
    background: linear-gradient(90deg, transparent, var(--rule), transparent);
  }
  .contact-line {
    display: flex; align-items: center; gap: 10px;
    font-size: 19px; color: var(--ink-white); font-weight: 400;
  }
  .contact-line svg { width: 18px; height: 18px; fill: var(--brand-blue); }
  .sep { color: var(--ink-white); }
</style>
</head>
<body>
<main class="stage">
  <section class="card card--front" aria-label="Card front">
    <div class="brand-lockup">
      <span class="brand-dot"></span>
      <span class="brand-name">QUARNETH</span>
    </div>
    <p class="tagline">POWER MEETS PRECISION</p>
  </section>

  <section class="card card--back" aria-label="Card back">
    <p class="back-brand">QUARNETH</p>
    <p class="identity">
      <span class="identity__name">DEREK OLSTOW</span>
      <span class="sep">|</span>
      <span class="identity__role">Director/Electrician</span>
    </p>
    <div class="divider"></div>
    <p class="contact-line">
      <svg viewBox="0 0 24 24" aria-hidden="true"><path d="M6.6 10.8a15.1 15.1 0 0 0 6.6 6.6l2.2-2.2a1 1 0 0 1 1-.25 11.4 11.4 0 0 0 3.6.57 1 1 0 0 1 1 1V20a1 1 0 0 1-1 1A17 17 0 0 1 3 4a1 1 0 0 1 1-1h3.5a1 1 0 0 1 1 1c0 1.25.2 2.45.57 3.57a1 1 0 0 1-.25 1z"/></svg>
      <span>021 387 9415</span>
      <span class="sep">|</span>
      <svg viewBox="0 0 24 24" aria-hidden="true"><path d="M12 2a7 7 0 0 0-7 7c0 5.25 7 13 7 13s7-7.75 7-13a7 7 0 0 0-7-7zm0 9.5A2.5 2.5 0 1 1 12 6.5a2.5 2.5 0 0 1 0 5z"/></svg>
      <span>Auckland</span>
    </p>
  </section>
</main>
</body>
</html>
```